Postcard Design Harlow Bend D to D

Residential Real Estate, we want to implement a mail campaign in an specific geographic area.We want to include Market information on the area and statistics of the real estate market.This piece is going to be deliver via mail service door to door.

Target Market(s)

Home owners that might be interested in selling their houses

Industry/Entity Type

Real Estate

Font styles to use
Sans Serif

Colors
ec1f27
f78f20

Requirements
Must have
• Attractive look
• Include the information that we just sent to you
• Clear graphics and tables
• Must include clear information about our group

```html
<!DOCTYPE html>
<html lang="en">
<head>
<meta charset="utf-8">
<title>Harlow Bend Market Report Postcard</title>
<link href="https://fonts.googleapis.com/css2?family=Arimo:wght@400;700&family=Roboto:wght@300;400;700;900&display=swap" rel="stylesheet">
<style>
:root{
  --red:#ec1f27;
  --wine:#a31c23;
  --orange:#f78f20;
  --ink:#333;
  --grey:#6d6d6d;
  --paper:#fff;
  --stage:#000;
}
*{box-sizing:border-box;margin:0;padding:0}
html,body{width:1200px;height:1200px;overflow:hidden;background:var(--stage)}
body{position:relative;font-family:"Arimo",Arial,sans-serif;color:var(--ink)}
.card{position:absolute;left:233px;width:730px;height:490px;background:var(--paper);overflow:hidden}
.front{top:103px}
.back{top:641px}
.abs{position:absolute}

/* FRONT */
.masthead{left:0;top:0;width:730px;height:130px;background:var(--wine);color:#fff;text-align:center;padding-top:36px}
.masthead h1{font-family:"Roboto",sans-serif;font-weight:300;font-size:31px;line-height:32px;letter-spacing:.2px}
.masthead h1 b{font-weight:900}
.masthead p{font-family:"Roboto",sans-serif;font-weight:400;font-size:24px;line-height:25px}
.masthead p b{font-weight:700}
.letter{left:0;top:130px;width:730px;height:172px;background:var(--orange);color:#fff;padding:12px 46px 0 46px;font-size:12.4px;line-height:15.5px}
.letter h2{font-style:italic;font-weight:700;font-size:15px;margin-bottom:6px}
.letter p{margin-bottom:15px}
.letter p:last-child{margin-bottom:0}
.facts{left:46px;top:302px;width:321px}
.facts h3{border:1px solid #555;border-bottom:none;font-family:"Roboto",sans-serif;font-weight:700;font-size:19px;color:#555;padding:4px 0 3px 32px;height:33px}
.facts h3 span{color:var(--red)}
.facts table{width:100%;border-collapse:collapse;color:#fff;font-weight:700;font-size:12.5px}
.facts td{height:18px;border:1px solid #fff;padding:0 0 0 32px}
.facts td.num{width:97px;text-align:center;padding:0}
.facts tr:nth-child(odd){background:var(--orange)}
.facts tr:nth-child(even){background:var(--wine)}
.quote{left:46px;top:416px;width:340px;font-size:11px;line-height:13px;color:var(--wine)}
.web{left:46px;top:445px;font-size:19px;color:#555}
.web b{color:var(--wine)}
.badges{left:323px;top:441px;display:flex;gap:12px}
.badge{width:38px;height:22px;background:#ddd}
.badge.round{width:22px;border-radius:50%}
.brand{right:51px;top:316px;text-align:right}
.brand-name{font-family:"Roboto",sans-serif;font-weight:300;font-size:27px;color:var(--wine);letter-spacing:-.3px}
.brand-sub{font-size:11px;color:var(--red);font-style:italic;margin-top:-6px;margin-right:22px}
.agent{right:51px;top:360px;text-align:right}
.agent-name{font-family:"Roboto",sans-serif;font-size:17px;color:var(--wine)}
.agent-role{font-family:"Roboto",sans-serif;font-size:12px;color:var(--orange)}
.contact{right:51px;top:399px;text-align:right;font-size:11.5px;line-height:13px;color:#333}
.contact .addr{font-weight:700;margin-bottom:3px}
.contact b{color:var(--wine)}

/* BACK */
.intro{left:34px;top:46px;width:336px;font-family:"Roboto",sans-serif;font-weight:300;font-size:14px;line-height:16px;color:#444;text-align:justify}
.intro p{margin-bottom:15px}
.section-bar{left:0;height:20px;background:var(--wine);color:#fff;font-family:"Roboto",sans-serif;font-weight:300;font-size:13px;padding:2px 0 0 33px}
.range-label{left:0;width:86px;background:var(--wine);color:#fff;font-size:9px;line-height:11px;padding:14px 0 0 38px}
.dom-tab{height:12px;background:var(--grey);color:#fff;font-size:8px;line-height:12px;padding-left:13px}
.grid{border-collapse:collapse;font-size:7.5px;color:#333;table-layout:fixed}
.grid th{background:var(--orange);color:#fff;font-weight:400;height:10px;border:1px solid #fff}
.grid th:first-child{font-weight:700}
.grid td{height:10.4px;border-left:1px solid var(--orange);border-bottom:1px solid #ccc;padding-left:4px}
.grid td:first-child{padding-left:12px;border-left:1px solid var(--red)}
.grid td.tot{text-align:center;font-weight:700;border-right:1px solid var(--red);padding:0}
.grid tr.sum td{background:var(--orange);color:#fff;text-align:center;padding:0;font-size:8.5px;border-color:#fff}
.grid{outline:1px solid var(--red)}
.stamp{left:596px;top:0;width:134px;height:126px;background:var(--red);color:#fff;font-weight:700;font-size:12.5px;text-align:center}
.stamp span{position:absolute;left:44px;top:33px;width:76px;line-height:15px}
.logo-mark{left:455px;top:44px;width:40px;height:40px;background:var(--wine)}
.logo-name{left:409px;top:90px;font-family:"Roboto",sans-serif;font-weight:300;font-size:16px;color:var(--wine)}
.logo-sub{left:497px;top:106px;font-size:7px;color:var(--red)}
.chart-title{left:404px;top:141px;width:221px;height:20px;background:var(--wine);color:#fff;font-family:"Roboto",sans-serif;font-weight:300;font-size:12px;line-height:20px;text-align:center}
.chart{left:397px;top:168px}
.trend{left:502px;top:297px;font-size:9px;color:#555}
.source{left:423px;top:307px;font-size:9px;color:#555}
.mail-zone{left:410px;top:334px;width:320px;height:156px;background:var(--red);color:#fff;font-weight:700;font-size:7px;text-align:center}
.mail-zone .note{position:absolute;left:88px;top:66px;width:166px;line-height:9px}
.mail-zone .foot{position:absolute;left:0;width:100%;top:141px}
</style>
</head>
<body>

<section class="card front">
  <header class="abs masthead">
    <h1>HARLOW BEND <b>MARKET REPORT</b></h1>
    <p>of Single Family <b>Sold</b> and <b>Active</b> Homes</p>
    <p>October Results <b>2015</b></p>
  </header>

  <div class="abs letter">
    <h2>Dear Harlow Bend Neighbor</h2>
    <p>We expect that this information will be useful for you to learn about the Real estate market in your neighborhood. There are 28 properties <b>“Active for Sale”</b> on the market, with an average price of <b><i>$303,589 USD</i></b> and <b><i>$101.06 USD per sf</i></b>. &nbsp;Average time on market for sale <b>63 days.</b></p>
    <p>In process, <b>“Pending to Close”</b> are 9 &nbsp;houses at average price of <b>$252,808 USD</b> with a sale price of <b>$103.11 per sf.</b> &nbsp;with <b>34 Days</b> on market.<br>The past 6 Months &nbsp;market behavior was as follows: 97 Houses sold at average price of <b>$263,545</b> with a sale price / sqf. of <b>$100.50</b></p>
  </div>

  <div class="abs facts">
    <h3>Harlow Bend <span>2014</span> Facts</h3>
    <table>
      <tr><td>Single Family Properties</td><td class="num">1,677</td></tr>
      <tr><td>Median Square Feet</td><td class="num">2,568</td></tr>
      <tr><td>Median Lot Square Feet</td><td class="num">7,689</td></tr>
      <tr><td>Median Year Built</td><td class="num">2007</td></tr>
    </table>
  </div>
  <p class="abs quote">“We will be glad to meet with you and have the opportunity to help you with your Real Estate requirements”</p>
  <p class="abs web">www.<b>themarlowegroup</b>.com</p>
  <div class="abs badges"><span class="badge"></span><span class="badge"></span><span class="badge round"></span></div>

  <div class="abs brand">
    <div class="brand-name">The Marlowe Group</div>
    <div class="brand-sub">Real Estate</div>
  </div>
  <div class="abs agent">
    <div class="agent-name">RENATA MARLOWE</div>
    <div class="agent-role">Realtor</div>
  </div>
  <div class="abs contact">
    <div class="addr">2250 Cedar Ridge Parkway Suite 3B<br>Alder Springs, TX 77390</div>
    <div>Phone: <b>281-555-0148</b></div>
    <div>Mobile: <b>281-555-0193</b></div>
    <div>Email: <b>renata@renatamarlowe.com</b></div>
  </div>
</section>

<section class="card back">
  <div class="abs intro">
    <p>Updated information to help you make a smart decision!</p>
    <p>If you are planning to SELL or BUY your home let us provide you with updated and accurate information.</p>
    <p>Let us help to maximize your profit in the most effective way following a secure and smooth journey.</p>
  </div>

  <div class="abs section-bar" style="top:187px;width:379px">ACTIVE ON THE MARKET</div>
  <div class="abs range-label" style="top:239px;height:75px">House Price Sold by Range of $50k</div>
  <div class="abs dom-tab" style="left:86px;top:215px;width:108px">DAYS ON MARKET</div>
  <table class="abs grid" style="left:86px;top:227px;width:295px">
    <colgroup><col style="width:76px"><col span="7" style="width:27.5px"><col style="width:26px"></colgroup>
    <tr><th>Sold Price</th><th>0-29</th><th>30-59</th><th>60-89</th><th>90-119</th><th>120-149</th><th>150-179</th><th>180-209</th><th>Total</th></tr>
    <tr><td>$150 -$199</td><td>1</td><td></td><td>1</td><td>1</td><td></td><td></td><td></td><td class="tot">3</td></tr>
    <tr><td>$200 -$249</td><td>2</td><td></td><td></td><td>1</td><td>1</td><td></td><td></td><td class="tot">4</td></tr>
    <tr><td>$250 - $299</td><td>1</td><td>3</td><td></td><td>2</td><td></td><td></td><td></td><td class="tot">6</td></tr>
    <tr><td>$300 -$ 349</td><td>5</td><td>2</td><td></td><td></td><td></td><td></td><td>2</td><td class="tot">9</td></tr>
    <tr><td>$350 - $399</td><td>2</td><td></td><td></td><td>1</td><td></td><td>1</td><td></td><td class="tot">4</td></tr>
    <tr><td>$400 - $449</td><td>1</td><td></td><td></td><td></td><td></td><td></td><td></td><td class="tot">1</td></tr>
    <tr><td>$450 - $499</td><td></td><td></td><td></td><td>1</td><td></td><td></td><td></td><td class="tot">1</td></tr>
    <tr class="sum"><td>Total</td><td>12</td><td>5</td><td>1</td><td>6</td><td>1</td><td>1</td><td>2</td><td>28</td></tr>
  </table>

  <div class="abs section-bar" style="top:339px;width:374px">SOLD PROPERTIES (PAST 6 MONTHS)</div>
  <div class="abs range-label" style="top:397px;height:52px;padding-top:2px;padding-left:33px">House Price Sold by Range of $50k</div>
  <div class="abs dom-tab" style="left:82px;top:369px;width:104px">DAYS ON MARKET</div>
  <table class="abs grid" style="left:78px;top:382px;width:305px">
    <colgroup><col style="width:84px"><col span="8" style="width:25px"><col style="width:21px"></colgroup>
    <tr><th>Sold Price</th><th>0-29</th><th>30-59</th><th>60-89</th><th>90-119</th><th>120-149</th><th>150-179</th><th>180-209</th><th>210-239</th><th>Total</th></tr>
    <tr><td>$170 -$219</td><td>23</td><td>3</td><td>3</td><td>1</td><td>2</td><td>1</td><td></td><td></td><td class="tot">33</td></tr>
    <tr><td>$220 -$ 269</td><td>11</td><td>5</td><td>5</td><td>1</td><td></td><td></td><td></td><td></td><td class="tot">22</td></tr>
    <tr><td>$270 - $319</td><td>10</td><td>5</td><td>5</td><td>1</td><td></td><td></td><td></td><td></td><td class="tot">21</td></tr>
    <tr><td>$320 -$369</td><td>9</td><td></td><td></td><td></td><td></td><td>1</td><td>1</td><td></td><td class="tot">13</td></tr>
    <tr><td>$370-$ 420</td><td>3</td><td>3</td><td>1</td><td></td><td>1</td><td></td><td></td><td></td><td class="tot">8</td></tr>
    <tr class="sum"><td>Total</td><td>56</td><td>16</td><td>14</td><td>3</td><td>3</td><td>2</td><td>1</td><td>2</td><td>97</td></tr>
  </table>

  <div class="abs stamp">
    <svg class="abs" style="left:0;top:0" width="134" height="126" viewBox="0 0 134 126" aria-hidden="true">
      <g stroke="#fff" stroke-width="1.5" fill="#fff">
        <line x1="26" y1="8" x2="26" y2="86"/>
        <polygon points="26,2 21,11 31,11"/><polygon points="26,92 21,83 31,83"/>
        <line x1="46" y1="90" x2="126" y2="90"/>
        <polygon points="40,90 49,85 49,95"/><polygon points="132,90 123,85 123,95"/>
      </g>
    </svg>
    <span>Stamp<br>1.25” inch</span>
  </div>

  <div class="abs logo-mark"></div>
  <div class="abs logo-name">The Marlowe Group</div>
  <div class="abs logo-sub">Real Estate</div>

  <div class="abs chart-title">The Historic Price per sqf. 2003 - 2014</div>
  <svg class="abs chart" width="230" height="128" viewBox="0 0 230 128" role="img" aria-label="Bar chart of historic price per square foot, 2003 to 2014">
    <g font-family="Arimo, sans-serif" font-size="5" fill="#333">
      <text x="0" y="10">100</text><text x="3" y="38">90</text><text x="3" y="65">80</text><text x="3" y="93">70</text><text x="3" y="120">60</text>
    </g>
    <g>
      <rect x="17" y="84.8" width="10" height="33.2" fill="#f78f20"/>
      <rect x="34" y="105.5" width="10" height="12.5" fill="#a31c23"/>
      <rect x="51" y="90.5" width="10" height="27.5" fill="#f78f20"/>
      <rect x="68" y="74" width="10" height="44" fill="#a31c23"/>
      <rect x="85" y="50.6" width="10" height="67.4" fill="#f78f20"/>
      <rect x="102" y="68.5" width="10" height="49.5" fill="#a31c23"/>
      <rect x="119" y="54.7" width="10" height="63.3" fill="#f78f20"/>
      <rect x="136" y="53.4" width="10" height="64.6" fill="#a31c23"/>
      <rect x="153" y="54.7" width="10" height="63.3" fill="#f78f20"/>
      <rect x="170" y="47.9" width="10" height="70.1" fill="#a31c23"/>
      <rect x="187" y="35.5" width="10" height="82.5" fill="#f78f20"/>
      <rect x="204" y="16.2" width="10" height="101.8" fill="#a31c23"/>
    </g>
    <g font-family="Arimo, sans-serif" font-size="4.6" fill="#333" text-anchor="middle">
      <text x="22" y="125">2003</text><text x="39" y="125">2004</text><text x="56" y="125">2005</text><text x="73" y="125">2006</text><text x="90" y="125">2007</text><text x="107" y="125">2008</text><text x="124" y="125">2009</text><text x="141" y="125">2010</text><text x="158" y="125">2011</text><text x="175" y="125">2012</text><text x="192" y="125">2013</text><text x="209" y="125">2014</text>
    </g>
  </svg>
  <div class="abs trend">Trend</div>
  <div class="abs source">*Data from Gulf Coast Association of Realtors</div>

  <div class="abs mail-zone">
    <svg class="abs" style="left:0;top:0" width="320" height="156" viewBox="0 0 320 156" aria-hidden="true">
      <g stroke="#fff" stroke-width="1" fill="#fff">
        <line x1="64" y1="8" x2="256" y2="8"/>
        <polygon points="60,8 67,5 67,11"/><polygon points="260,8 253,5 253,11"/>
        <line x1="260" y1="14" x2="260" y2="150"/>
        <polygon points="260,10 257,17 263,17"/><polygon points="260,154 257,147 263,147"/>
      </g>
    </svg>
    <p class="note">This area needs to remain BLANK WHITE for mailing puposes. Please DO NOT place any graphics, color or text in this area.</p>
    <p class="foot">Barcode &amp; Post Office Marking Area</p>
  </div>
</section>

</body>
</html>
```